Sundeck construction company in need of creative business cards

We provide all round services for a variety of different deck types. Our core 3 things are vinyl decking, aluminum railings and wood decks. We want to use 3 different solid 15 gauge plastic cards with one side having a picture of either a railing, vinyl deck or a wood deck (then depending on what the client wants we can give them the card that best suites there needs) we would also want our logo layered overtop of the picture. On the other side we would have our logo and info
Updates

Sorry was busy in meetings all day will be reviewing now

1 I had posted wrong picture for railings please revise
2 Address is 2243-10562 Bramblefield Road
                    Richmond B.C.
V6K 3M2

We like the front design of #1566013

Target Market(s)

Single family residential

Industry/Entity Type

Construction

Requirements
Must have
• 3 different pictures on back of card for vinyl deckin, aluminum railings and wood decks

```html
<!DOCTYPE html>
<html lang="en">
<head>
<meta charset="utf-8">
<title>Cedarline Sundecks Business Card</title>
<link href="https://fonts.googleapis.com/css2?family=Arimo:wght@400;700&display=swap" rel="stylesheet">
<style>
  :root {
    --page-bg: #e6e7e9;
    --navy: #2b2f5e;
    --green-dark: #0f6a36;
    --green-light: #7dbf48;
    --leaf: #4c9a3a;
    --white: #ffffff;
    --photo-sky: #9fb0d8;
    --photo-water: #8fb0b8;
    --photo-green: #7c9e5a;
  }
  * { box-sizing: border-box; margin: 0; padding: 0; }
  html, body { width: 1200px; height: 861px; overflow: hidden; }
  body {
    background: var(--page-bg);
    font-family: "Arimo", Arial, sans-serif;
    position: relative;
  }
  .card {
    position: absolute;
    top: 276px;
    width: 540px;
    height: 309px;
    overflow: hidden;
    box-shadow: 0 6px 18px rgba(0,0,0,.25);
    background: var(--white);
  }
  .card--front { left: 40px; }
  .card--back { left: 620px; }

  .front-photo {
    position: absolute; inset: 0;
    background:
      linear-gradient(180deg, rgba(255,255,255,0) 45%, rgba(255,255,255,.92) 88%),
      linear-gradient(180deg, var(--photo-sky) 0%, #c7b9d6 28%, var(--photo-water) 48%, var(--photo-green) 70%, #a9b39b 100%);
  }
  .front-brand {
    position: absolute; left: 64px; top: 256px;
    display: flex; align-items: center; gap: 10px;
  }
  .brand-dot {
    width: 18px; height: 18px; border-radius: 50%;
    background: var(--leaf);
  }
  .brand-name {
    color: var(--navy);
    font-weight: 400;
    letter-spacing: 1px;
    text-transform: uppercase;
    font-size: 21px;
  }

  .back-head {
    position: absolute; left: 0; top: 0; width: 100%; height: 133px;
    display: flex; align-items: center; justify-content: center; gap: 14px;
    background: var(--white);
  }
  .back-head .brand-dot { width: 26px; height: 26px; }
  .back-head .brand-name { font-size: 25px; }
  .back-stripe {
    position: absolute; left: 0; top: 133px; width: 100%; height: 6px;
    background: var(--navy);
  }
  .back-body {
    position: absolute; left: 0; top: 139px; width: 100%; bottom: 0;
    background: linear-gradient(180deg, var(--green-dark) 0%, #2f8a3a 45%, var(--green-light) 100%);
    color: var(--white);
  }
  .holder-name {
    position: absolute; left: 46px; top: 30px;
    font-size: 30px; font-weight: 700;
  }
  .address {
    position: absolute; left: 52px; top: 104px;
    display: flex; gap: 12px; font-size: 14px; line-height: 19px;
  }
  .contacts {
    position: absolute; left: 344px; top: 22px;
    list-style: none; font-size: 13px;
  }
  .contacts li {
    display: flex; align-items: center; gap: 9px;
    height: 26px;
  }
  .icon { width: 20px; height: 20px; flex: none; }
</style>
</head>
<body>
  <section class="card card--front">
    <div class="front-photo" role="img" aria-label="Photograph of a balcony deck with lounge chairs and glass railing overlooking a city marina and high-rise towers"></div>
    <div class="front-brand">
      <span class="brand-dot"></span>
      <span class="brand-name">Cedarline Sundecks</span>
    </div>
  </section>

  <section class="card card--back">
    <header class="back-head">
      <span class="brand-dot"></span>
      <span class="brand-name">Cedarline Sundecks</span>
    </header>
    <div class="back-stripe"></div>
    <div class="back-body">
      <h1 class="holder-name">Daniel Whitford</h1>
      <div class="address">
        <svg class="icon" viewBox="0 0 20 20" aria-hidden="true">
          <circle cx="10" cy="10" r="9" fill="none" stroke="#fff" stroke-width="1.5"/>
          <path d="M10 4.5a3.5 3.5 0 0 0-3.5 3.5c0 2.6 3.5 7 3.5 7s3.5-4.4 3.5-7A3.5 3.5 0 0 0 10 4.5z" fill="#fff"/>
          <circle cx="10" cy="8" r="1.3" fill="#2f8a3a"/>
        </svg>
        <p>2243-10562 Bramblefield Road<br>Richmond B.C.<br>V6K 3M2</p>
      </div>
      <ul class="contacts">
        <li>
          <svg class="icon" viewBox="0 0 20 20" aria-hidden="true"><circle cx="10" cy="10" r="9" fill="none" stroke="#fff" stroke-width="1.5"/><path d="M6.5 5.5l2 0 1 2.5-1.3 1a6 6 0 0 0 2.8 2.8l1-1.3 2.5 1v2c-4.5.3-8.3-3.5-8-8z" fill="#fff"/></svg>
          604-555-0142
        </li>
        <li>
          <svg class="icon" viewBox="0 0 20 20" aria-hidden="true"><circle cx="10" cy="10" r="9" fill="none" stroke="#fff" stroke-width="1.5"/><rect x="7" y="4.5" width="6" height="11" rx="1" fill="none" stroke="#fff" stroke-width="1.3"/><circle cx="10" cy="13.5" r=".8" fill="#fff"/></svg>
          604-555-0187
        </li>
        <li>
          <svg class="icon" viewBox="0 0 20 20" aria-hidden="true"><circle cx="10" cy="10" r="9" fill="none" stroke="#fff" stroke-width="1.5"/><rect x="5.5" y="8" width="9" height="5" rx="1" fill="#fff"/><rect x="7" y="5" width="6" height="3" fill="none" stroke="#fff" stroke-width="1.2"/><rect x="7" y="12" width="6" height="3" fill="#fff"/></svg>
          604-555-0163
        </li>
        <li>
          <svg class="icon" viewBox="0 0 20 20" aria-hidden="true"><circle cx="10" cy="10" r="9" fill="none" stroke="#fff" stroke-width="1.5"/><rect x="5.5" y="6.5" width="9" height="7" fill="none" stroke="#fff" stroke-width="1.3"/><path d="M5.5 6.5l4.5 4 4.5-4" fill="none" stroke="#fff" stroke-width="1.3"/></svg>
          daniel@cedarlinevinyl.com
        </li>
        <li>
          <svg class="icon" viewBox="0 0 20 20" aria-hidden="true"><circle cx="10" cy="10" r="9" fill="none" stroke="#fff" stroke-width="1.5"/><rect x="5.5" y="6" width="9" height="6.5" fill="none" stroke="#fff" stroke-width="1.3"/><path d="M8 14.5h4" stroke="#fff" stroke-width="1.3"/></svg>
          www.cedarlinevinyl.com
        </li>
      </ul>
    </div>
  </section>
</body>
</html>
```